175th Anniversary of Family Owned Funeral Home Pole Banners

We are family owned and operated funeral home in the Greater Cincinnati area and operate 3 funeral homes and a cremation center and we will be celebrating our 175th anniversary in 2015. The communities we serve look to us as leaders in the community and we are very well recognized. In preparation for next year, part of our planning includes placing pole banners in our local communities and our funeral home parking areas. The banner dimensions will be 30 x 60. We need for the banners to display a great message of tradition and excellence. Our website is www.brackenholloway.com I have uploaded an example of a pole banner as well as our logo(s).
Updates
Original artwork has been uploaded if needed.
Industry/Entity Type
Funeral Home

```html
<!DOCTYPE html>
<html lang="en">
<head>
<meta charset="utf-8">
<title>175th Anniversary Pole Banner – Bracken Holloway</title>
<link rel="stylesheet" href="https://fonts.googleapis.com/css2?family=Lora:ital,wght@0,400;1,400&display=swap">
<style>
  :root {
    --page: #ffffff;
    --banner-white: #ffffff;
    --panel-light: #7db8dd;
    --panel-mid: #4f8db6;
    --panel-deep: #2b6990;
    --band: #4a7fa3;
    --wordmark: #3d6e96;
    --ink-light: #ffffff;
  }
  * { margin: 0; padding: 0; box-sizing: border-box; }
  html, body { width: 1200px; height: 1000px; overflow: hidden; background: var(--page); }
  body { position: relative; font-family: "Lora", Georgia, serif; }

  .banner {
    position: absolute; left: 369px; top: 38px; width: 462px; height: 924px;
    background: var(--banner-white);
    box-shadow: 0 6px 18px rgba(0,0,0,0.18);
  }
  .hero-panel {
    position: absolute; left: 23px; top: 24px; width: 416px; height: 698px;
    background: radial-gradient(ellipse 70% 55% at 50% 22%, var(--panel-light) 0%, var(--panel-mid) 55%, var(--panel-deep) 100%);
    color: var(--ink-light); text-align: center;
  }
  .anniv-our {
    position: absolute; top: 8px; left: 0; right: 0;
    font-style: italic; font-size: 40px; line-height: 1;
  }
  .anniv-frame {
    position: absolute; left: 68px; top: 52px; width: 280px; height: 210px;
    border-radius: 50%;
    background: radial-gradient(ellipse at center, rgba(255,255,255,0.10) 0%, rgba(255,255,255,0.28) 62%, rgba(255,255,255,0.05) 72%, transparent 74%);
  }
  .anniv-number {
    position: absolute; top: 108px; left: 0; right: 0;
    font-size: 54px; line-height: 1;
  }
  .anniv-years {
    position: absolute; top: 168px; left: 0; right: 0;
    font-size: 26px; line-height: 1;
  }
  .anniv-label {
    position: absolute; top: 264px; left: 0; right: 0;
    font-style: italic; font-size: 46px; line-height: 1; letter-spacing: 1px;
  }
  .mark-spot {
    position: absolute; left: 138px; top: 400px; width: 140px; height: 140px;
    border-radius: 50%; border: 4px solid var(--ink-light);
  }
  .wordmark {
    position: absolute; top: 736px; left: 0; right: 0; text-align: center;
    color: var(--wordmark); font-size: 44px; line-height: 1.2;
  }
  .service-band {
    position: absolute; left: 0; bottom: 0; width: 100%; height: 107px;
    background: var(--band); color: var(--ink-light);
    display: flex; flex-direction: column; justify-content: center; align-items: center;
    font-style: italic; font-size: 26px; line-height: 1.35;
  }
</style>
</head>
<body>
  <div class="banner">
    <section class="hero-panel">
      <div class="anniv-our">our</div>
      <div class="anniv-frame" role="img" aria-label="Ornamental scrollwork frame around the anniversary number"></div>
      <div class="anniv-number">175</div>
      <div class="anniv-years">years</div>
      <div class="anniv-label">anniversary</div>
      <div class="mark-spot"></div>
    </section>
    <div class="wordmark">Bracken Holloway</div>
    <div class="service-band">
      <span>Family Funeral Homes</span>
      <span>&amp; Cremation Center</span>
    </div>
  </div>
</body>
</html>
```